File Download Website

We are looking for a design for a file download website. Our objective is to allow users to upload/browse/download files. This means we need 3 different pages.
The upload page should allow users to upload a file, we are looking for creative designs, a file box with a browse button next to it is already out there so the design must bring something new.
The browse page should display a users files/folders.
The download page should allow the user to download a file.
We do not require any code, only design. The designer is given complete freedom over the design, you may go about it however you like. This is a test of creativity, whoever this project goes to will definitely be given more work in the near future.
Example of a well designed file download website: quelvanto.com
Target Market(s)
15-30 year old people
Industry/Entity Type
Work
Look and feel
Each slider illustrates characteristics of the customer's brand and the style your logo design should communicate.

```html
<!DOCTYPE html>
<html lang="en">
<head>
<meta charset="utf-8">
<title>Stashvault – Share your files</title>
<link href="https://fonts.googleapis.com/css2?family=Open+Sans:wght@400;600;700;800&family=Permanent+Marker&family=Nothing+You+Could+Do&display=swap" rel="stylesheet">
<style>
:root{
  --top-strip:#1d4a6b;
  --sky:#3d9ad9;
  --sky-light:#6dbbef;
  --sky-deep:#2b7fc1;
  --band:#2f84c6;
  --nav-text:#1f6fae;
  --white:#ffffff;
  --orange:#f5a623;
  --orange-deep:#e38b12;
  --pale:#dcecf9;
  --link:#2f86c9;
  --mid-col:#3c95d8;
  --footer:#23557a;
  --footer-text:#d7e7f3;
  --bottom:#163a55;
}
*{margin:0;padding:0;box-sizing:border-box}
html,body{width:847px;height:1200px;overflow:hidden}
body{font-family:"Open Sans",Arial,sans-serif;background:var(--sky);position:relative}
.abs{position:absolute}

.top-strip{left:0;top:0;width:847px;height:14px;background:var(--top-strip)}
.login-btn{left:770px;top:14px;width:44px;height:14px;background:var(--top-strip);color:#cfe3f2;font-size:8px;font-weight:600;text-align:center;line-height:14px;border-radius:0 0 3px 3px}

.header{left:0;top:14px;width:847px;height:260px;background:radial-gradient(ellipse at 40% 40%,#4aa6e3 0%,#3891d3 60%,#2f86c8 100%)}
.brand{left:62px;top:110px;display:flex;align-items:center;gap:12px}
.brand-mark{width:34px;height:34px;background:var(--sky-deep);border-radius:4px}
.brand-name{font-size:40px;font-weight:700;color:var(--white);letter-spacing:-0.5px;line-height:1}
.slogan{left:108px;top:160px;font-size:12px;color:#e6f2fb;font-weight:600}

.tagline{left:500px;top:60px;width:314px;text-align:right;color:var(--white);font-family:"Nothing You Could Do",cursive}
.tagline .line1{font-size:26px;letter-spacing:1px}
.tagline .line2{font-size:40px;letter-spacing:3px;margin-top:2px;margin-right:20px}
.signup{left:534px;top:174px;font-size:22px;color:var(--white)}
.signup small{font-size:12px;margin-left:8px;color:#dcecf8}
.social-btn{left:636px;top:170px;width:182px;height:36px;background:#2a6fae;border-radius:3px;display:flex;align-items:center;color:var(--white);font-size:14px}
.social-btn .sq{width:34px;height:36px;background:#235f98;margin-right:10px;border-radius:3px 0 0 3px}
.social-btn b{font-weight:700;margin-left:4px}

.header-edge{left:0;top:274px;width:847px;height:6px;background:var(--band)}
.nav{left:0;top:280px;width:847px;height:52px;background:var(--white)}
.nav a{position:absolute;top:0;height:52px;line-height:52px;font-size:14px;font-weight:700;color:var(--nav-text);text-decoration:none;letter-spacing:.5px}
.nav a.active{background:var(--sky-deep);color:var(--white);text-align:center;width:100px}

.hero{left:0;top:332px;width:847px;height:373px;background:radial-gradient(ellipse 320px 260px at 423px 170px,#dff0fc 0%,#9fd0f1 30%,#5aaee6 65%,#3b93d4 100%)}
.browse-title{left:0;top:382px;width:847px;text-align:center;font-family:"Permanent Marker",cursive;font-size:46px;color:var(--orange);line-height:1}
.browse-sub{left:0;top:436px;width:847px;text-align:center;font-family:"Permanent Marker",cursive;font-size:10px;color:var(--orange-deep)}
.search{left:202px;top:475px;width:430px;height:70px;background:linear-gradient(#f6f6f6,#d6d6d6);border-radius:6px;box-shadow:inset 0 2px 4px rgba(0,0,0,.25),0 1px 0 #fff}
.search-btn{left:595px;top:458px;width:104px;height:104px;border-radius:50%;background:radial-gradient(circle at 45% 35%,#ffffff,#dcdcdc 70%,#c6c6c6);box-shadow:0 3px 8px rgba(0,0,0,.3)}
.search-btn svg{position:absolute;left:27px;top:27px}
.count-pre{left:0;top:560px;width:847px;text-align:center;font-family:"Permanent Marker",cursive;font-size:11px;color:var(--orange-deep)}
.count{left:0;top:578px;width:847px;text-align:center;font-family:"Permanent Marker",cursive;font-size:70px;color:var(--orange);line-height:1}
.count-post{left:0;top:660px;width:847px;text-align:center;font-family:"Permanent Marker",cursive;font-size:18px;color:var(--orange)}

.col-head{top:705px;height:47px;line-height:47px;color:var(--white);font-size:19px;font-weight:600;letter-spacing:.5px;background:rgba(30,110,175,.35)}
.col-left{left:0;top:752px;width:296px;height:271px;background:var(--pale)}
.col-mid{left:296px;top:752px;width:285px;height:271px;background:linear-gradient(#2f86c9,#5aaee6)}
.col-right{left:581px;top:752px;width:266px;height:271px;background:var(--pale)}
.file-list{list-style:none}
.file-list li{position:absolute;display:flex;align-items:flex-start;gap:10px;left:0}
.file-list .name{font-size:15px;line-height:18px}
.file-list .size{font-size:11px;font-weight:700;line-height:13px}
.col-left .name{color:var(--link)}
.col-left .size{color:#3b6e94}
.col-mid .name{color:var(--white);font-weight:700}
.col-mid .size{color:#e2f0fa}
.col-mid li.hover{background:#8ec6ee;color:var(--orange)}
.col-mid li.hover .name,.col-mid li.hover .size{color:var(--orange-deep)}
.blog{left:614px;top:778px;width:210px;color:var(--link);font-size:14px;line-height:19px}
.blog a{color:var(--link)}

.footer{left:0;top:1023px;width:847px;height:157px;background:var(--footer)}
.footer-col{position:absolute;top:16px;color:var(--footer-text)}
.footer-col h4{font-size:17px;font-weight:400;color:var(--white);margin-bottom:10px}
.footer-col p{font-size:12px;line-height:27px}
.bottom{left:0;top:1180px;width:847px;height:20px;background:var(--bottom);color:#cfe0ee;font-size:11px;text-align:center;line-height:20px}
</style>
</head>
<body>
<div class="abs top-strip"></div>
<div class="abs header"></div>
<div class="abs login-btn">LOG IN</div>

<div class="abs brand"><span class="brand-mark"></span><span class="brand-name">Stashvault</span></div>
<div class="abs slogan">this is slogan</div>

<div class="abs tagline"><div class="line1">Start sharing your files</div><div class="line2">RIGHT NOW!</div></div>
<div class="abs signup">Sign up<small>or</small></div>
<div class="abs social-btn"><span class="sq"></span>Login with<b>Friendloop</b></div>

<div class="abs header-edge"></div>
<nav class="abs nav">
  <a class="active" href="#" style="left:224px">HOME</a>
  <a href="#" style="left:350px">ABOUT</a>
  <a href="#" style="left:438px">SECURITY</a>
  <a href="#" style="left:540px">CONTACT</a>
</nav>

<section class="abs hero"></section>
<div class="abs browse-title">BROWSE</div>
<div class="abs browse-sub">OVER 100K FILES</div>
<div class="abs search"></div>
<div class="abs search-btn">
  <svg width="50" height="50" viewBox="0 0 50 50"><circle cx="20" cy="20" r="13" fill="#bfe0f5" stroke="#4a7ea6" stroke-width="4"/><line x1="30" y1="30" x2="44" y2="44" stroke="#2f5f85" stroke-width="7" stroke-linecap="round"/></svg>
</div>
<div class="abs count-pre">UPLOADED BY</div>
<div class="abs count">1647</div>
<div class="abs count-post">VERIFIED USERS!</div>

<div class="abs col-head" style="left:0;width:296px;padding-left:32px">LATEST DOWNLOADS</div>
<div class="abs col-head" style="left:296px;width:285px;text-align:center;background:rgba(30,110,175,.5)">JUST UPLOADED!</div>
<div class="abs col-head" style="left:581px;width:266px;padding-left:33px">FROM OUR BLOG</div>

<div class="abs col-left">
  <ul class="file-list">
    <li style="left:33px;top:25px"><svg width="30" height="30" viewBox="0 0 30 30"><path d="M4 2h14l8 8v18H4z" fill="none" stroke="#2f86c9" stroke-width="2"/><rect x="2" y="16" width="20" height="9" fill="#2f86c9"/><text x="12" y="23" font-size="7" fill="#fff" text-anchor="middle" font-family="Open Sans,sans-serif">7z</text></svg><div><div class="name">UP-ed 7zip file preview</div><div class="size">(2,6MB)</div></div></li>
    <li style="left:33px;top:73px"><svg width="30" height="30" viewBox="0 0 30 30"><path d="M4 2h14l8 8v18H4z" fill="none" stroke="#2f86c9" stroke-width="2"/><rect x="2" y="16" width="20" height="9" fill="#2f86c9"/><text x="12" y="23" font-size="7" fill="#fff" text-anchor="middle" font-family="Open Sans,sans-serif">AVI</text></svg><div><div class="name">UP-ed AVI File Preview</div><div class="size">(57,2MB)</div></div></li>
    <li style="left:33px;top:122px"><svg width="30" height="30" viewBox="0 0 30 30"><path d="M4 2h14l8 8v18H4z" fill="none" stroke="#2f86c9" stroke-width="2"/><rect x="2" y="16" width="20" height="9" fill="#2f86c9"/><text x="12" y="23" font-size="7" fill="#fff" text-anchor="middle" font-family="Open Sans,sans-serif">ISO</text></svg><div><div class="name">UP-ed ISO File Preview</div><div class="size">(698,4MB)</div></div></li>
    <li style="left:33px;top:172px"><svg width="30" height="30" viewBox="0 0 30 30"><path d="M4 2h14l8 8v18H4z" fill="none" stroke="#2f86c9" stroke-width="2"/><rect x="2" y="16" width="20" height="9" fill="#2f86c9"/><text x="12" y="23" font-size="7" fill="#fff" text-anchor="middle" font-family="Open Sans,sans-serif">EXE</text></svg><div><div class="name">UP-ed EXE File Preview</div><div class="size">(7,9MB)</div></div></li>
  </ul>
</div>

<div class="abs col-mid">
  <ul class="file-list">
    <li style="left:0;top:20px;width:285px;padding:4px 0 4px 20px"><svg width="30" height="30" viewBox="0 0 30 30"><path d="M4 2h14l8 8v18H4z" fill="none" stroke="#fff" stroke-width="2"/><rect x="2" y="16" width="20" height="9" fill="#fff"/><text x="12" y="23" font-size="7" fill="#2f86c9" text-anchor="middle" font-family="Open Sans,sans-serif">7z</text></svg><div><div class="name">DL-ed 7zip File Preview</div><div class="size">(2,6MB)</div></div></li>
    <li class="hover" style="left:0;top:68px;width:285px;padding:4px 0 8px 20px"><svg width="30" height="30" viewBox="0 0 30 30"><path d="M4 2h14l8 8v18H4z" fill="none" stroke="#e38b12" stroke-width="2"/><rect x="2" y="16" width="20" height="9" fill="#e38b12"/><text x="12" y="23" font-size="7" fill="#fff" text-anchor="middle" font-family="Open Sans,sans-serif">AVI</text></svg><div><div class="name">DL-ed AVI File Preview</div><div class="size">(57,2MB)</div></div></li>
    <li style="left:0;top:118px;width:285px;padding:4px 0 4px 20px"><svg width="30" height="30" viewBox="0 0 30 30"><path d="M4 2h14l8 8v18H4z" fill="none" stroke="#fff" stroke-width="2"/><rect x="2" y="16" width="20" height="9" fill="#fff"/><text x="12" y="23" font-size="7" fill="#2f86c9" text-anchor="middle" font-family="Open Sans,sans-serif">ISO</text></svg><div><div class="name">DL-ed ISO File Preview</div><div class="size">(698,4MB)</div></div></li>
    <li style="left:0;top:168px;width:285px;padding:4px 0 4px 20px"><svg width="30" height="30" viewBox="0 0 30 30"><path d="M4 2h14l8 8v18H4z" fill="none" stroke="#fff" stroke-width="2"/><rect x="2" y="16" width="20" height="9" fill="#fff"/><text x="12" y="23" font-size="7" fill="#2f86c9" text-anchor="middle" font-family="Open Sans,sans-serif">EXE</text></svg><div><div class="name">DL-ed EXE File Preview</div><div class="size">(7,9MB)</div></div></li>
  </ul>
</div>

<div class="abs col-right"></div>
<div class="abs blog">Our website is currently under construction.<br>Please be patient.<br>Read more about this <a href="#">HERE!</a></div>

<footer class="abs footer">
  <div class="footer-col" style="left:264px"><h4>Company</h4><p>About Us</p><p>Our Team</p><p>Press</p></div>
  <div class="footer-col" style="left:378px"><h4>Tools</h4><p>API</p></div>
  <div class="footer-col" style="left:450px"><h4>Upgrade</h4><p>Professional</p><p>Business</p></div>
  <div class="footer-col" style="left:543px"><h4>Support</h4><p>Contact Us</p></div>
</footer>
<div class="abs bottom">2013.</div>
</body>
</html>
```